Brenwick Structures Construction Company Seeking Modern Website

We are a small construction company wanting to create a web presence. We don't have much in the way of current content but will get photos as they come in. Attached is a picture of our business card.
The pages we would like on the menu are:
Home
Portfolio
Product Specs
Testimonials
Our Process
Contact
Some designs we like are:
http://www.tovandrafters.example/
http://www.qrkframes.example/
http://harnestshed.example/
http://pellowbarns.example/
Not much requirements other than that so feel free to be creative!
Target Market(s)
Construction
Commercial and Residential Buildings
Industry/Entity Type
Construction Company
Number of Pages Required
5+ page

```html
<!DOCTYPE html>
<html lang="en">
<head>
<meta charset="utf-8">
<title>Brenwick Structures</title>
<link rel="stylesheet" href="https://fonts.googleapis.com/css2?family=Montserrat:wght@400;500;600;700&family=Open+Sans:ital,wght@0,400;0,600;1,400&display=swap">
<style>
:root{
  --blue:#1a9ad6;
  --red:#d9342b;
  --ink:#2f2f2f;
  --text:#555;
  --muted:#999;
  --pale:#f3f3f3;
  --footer:#2b2b2b;
  --footer-dark:#202020;
  --white:#fff;
}
*{margin:0;padding:0;box-sizing:border-box}
html,body{width:1200px;height:2270px;overflow:hidden}
body{position:relative;background:var(--white);font-family:"Open Sans",Arial,sans-serif;color:var(--text)}
.abs{position:absolute}
.topbar{left:0;top:0;width:1200px;height:30px;background:var(--blue);color:var(--white);font-size:12px}
.topbar span{position:absolute;top:8px;display:flex;align-items:center;gap:6px}
.header{left:0;top:30px;width:1200px;height:123px;background:var(--white)}
.brand{position:absolute;left:98px;top:38px;display:flex;align-items:center;gap:10px}
.brand-mark{width:26px;height:26px;background:var(--blue)}
.brand-name{font-family:"Montserrat",sans-serif;font-weight:700;font-size:22px;color:var(--ink)}
.tagline{position:absolute;left:98px;top:86px;font-size:9px;font-weight:600;color:var(--ink)}
.nav a{position:absolute;top:59px;font-family:"Montserrat",sans-serif;font-size:11.5px;font-weight:600;color:var(--ink);text-decoration:none;letter-spacing:.2px}
.nav a.active{color:var(--blue)}
.nav a.active::after{content:"";position:absolute;left:0;right:0;top:20px;height:3px;background:var(--red)}
.hero{left:0;top:153px;width:1200px;height:513px;background:linear-gradient(180deg,#3f8fd8 0%,#8fc0e8 30%,#c9b98f 55%,#7f9a55 80%,#5f7d3a 100%)}
.hero-title{left:177px;top:512px;font-family:"Montserrat",sans-serif;color:var(--white);font-size:25px;line-height:34px;font-weight:400}
.hero-title b{font-weight:700}
.btn{left:176px;top:587px;width:127px;height:36px;background:var(--blue);color:var(--white);font-size:12.5px;display:flex;align-items:center;justify-content:center;border-radius:2px}
.section-title{left:0;width:1200px;text-align:center;font-family:"Montserrat",sans-serif;font-size:26px;font-weight:600;color:var(--ink)}
.section-title em{font-style:normal;color:var(--blue)}
.intro{left:150px;top:764px;width:900px;text-align:center;font-size:12px;line-height:22px}
.card{top:830px;width:477px;height:246px;background:#e6e6e6;padding:7px;box-shadow:0 20px 18px -14px rgba(0,0,0,.25)}
.card .photo{width:100%;height:100%;position:relative}
.card .label{position:absolute;left:0;bottom:0;width:100%;height:42px;background:rgba(40,40,40,.55);color:var(--white);font-family:"Montserrat",sans-serif;font-weight:600;font-size:18px;display:flex;align-items:center;justify-content:center}
.projects{left:0;top:1132px;width:1200px;height:422px;background:var(--pale)}
.filters{left:0;top:1258px;width:1200px;display:flex;justify-content:center;gap:28px;font-family:"Montserrat",sans-serif;font-size:11.5px;font-weight:500;color:var(--ink)}
.filters span.active{color:var(--red);position:relative}
.filters span.active::after{content:"";position:absolute;left:-2px;right:-2px;top:22px;height:2px;background:var(--red)}
.tile{top:1312px;width:243px;height:190px}
.tile-overlay{display:flex;flex-direction:column;align-items:center;justify-content:center;color:var(--white);font-family:"Montserrat",sans-serif;font-weight:600;gap:12px}
.tile-overlay .t1{font-size:13px;border-bottom:1px solid var(--white);padding-bottom:3px}
.tile-overlay .t2{font-size:10.5px}
.quote{top:1670px;width:480px;height:121px;background:#f7f7f7;border:1px solid #e6e6e6}
.quote p{position:absolute;left:74px;top:28px;width:390px;font-size:11.5px;font-style:italic;line-height:20px;color:#777}
.quote .mark{position:absolute;left:20px;top:24px;font-family:Georgia,serif;font-size:60px;line-height:50px;color:#d6d6d6}
.quote .tail{position:absolute;left:58px;bottom:-16px;width:0;height:0;border-left:0 solid transparent;border-right:18px solid transparent;border-top:16px solid #e6e6e6}
.quote .tail::after{content:"";position:absolute;left:1px;top:-17px;border-right:16px solid transparent;border-top:15px solid #f7f7f7}
.avatar{width:80px;height:80px;border-radius:50%;border:1px solid #e2e2e2;background:linear-gradient(180deg,#eef2f6,#c9d4de)}
.person{font-size:15px;font-weight:600;color:var(--ink)}
.role{font-size:10.5px;color:var(--muted)}
.footer{left:0;top:1970px;width:1200px;height:248px;background:var(--footer);color:#d8d8d8;font-size:12px}
.fcol{position:absolute;top:44px}
.fcol h4{font-family:"Montserrat",sans-serif;font-weight:500;font-size:17px;color:var(--white);margin-bottom:12px}
.fcol li{list-style:none;line-height:23.5px}
.about p{line-height:21px;width:200px}
.social li{display:flex;align-items:center;gap:8px;line-height:35px}
.social i{width:24px;height:24px;border:1px solid #777;display:inline-block}
.contact-line{display:flex;align-items:center;gap:10px}
.bottom{left:0;top:2218px;width:1200px;height:52px;background:var(--footer-dark);color:#bbb;font-size:11px;text-align:center;line-height:52px}
</style>
</head>
<body>

<div class="abs topbar">
  <span style="left:98px"><svg width="10" height="13" viewBox="0 0 10 13"><path d="M5 0a5 5 0 0 0-5 5c0 3.5 5 8 5 8s5-4.5 5-8a5 5 0 0 0-5-5zm0 7a2 2 0 1 1 0-4 2 2 0 0 1 0 4z" fill="#fff"/></svg>24 Harbor Lane, Kestrel Bay, State 7021</span>
  <span style="left:418px"><svg width="14" height="10" viewBox="0 0 14 10"><rect width="14" height="10" fill="#fff"/><path d="M0 0l7 5 7-5" stroke="#1a9ad6" fill="none"/></svg>hello@brenwick.example</span>
  <span style="left:958px"><svg width="11" height="11" viewBox="0 0 11 11"><path d="M2 0l2 3-1 1.5a7 7 0 0 0 3.5 3.5L8 7l3 2-1.5 2C5 11 0 6 0 1.5z" fill="#fff"/></svg>+1 555 014 2290</span>
</div>

<header class="abs header">
  <div class="brand"><span class="brand-mark"></span><span class="brand-name">Brenwick Structures</span></div>
  <div class="tagline">Building Dreams, So You Can Build Memories</div>
  <nav class="nav">
    <a href="#" class="active" style="left:527px">HOME</a>
    <a href="#" style="left:588px">PORTFOLIO</a>
    <a href="#" style="left:679px">PRODUCT SPECS</a>
    <a href="#" style="left:799px">TESTIMONIALS</a>
    <a href="#" style="left:905px">OUR PROCESS</a>
    <a href="#" style="left:1011px">CONTACT</a>
    <svg style="position:absolute;left:1090px;top:58px" width="12" height="12" viewBox="0 0 12 12"><circle cx="5" cy="5" r="3.8" stroke="#2f2f2f" stroke-width="2" fill="none"/><path d="M8 8l3 3" stroke="#2f2f2f" stroke-width="2"/></svg>
  </nav>
</header>

<section class="abs hero" role="img" aria-label="Two-storey family home with front porch, garage and flowering garden under blue sky"></section>
<div class="abs hero-title">COMMERCIAL CONSTRUCTION AND<br><b>RESIDENTIAL BUILDINGS.</b></div>
<div class="abs btn">View more</div>

<h2 class="abs section-title" style="top:714px">WELCOME TO <em>BRENWICK STRUCTURES</em></h2>
<p class="abs intro">Lorem Ipsum is simply dummy text of the printing and typesetting industry. Lorem Ipsum has been the industry's standard dummy text ever since the 1500s,<br>when an unknown printer took a galley of type and scrambled it to make a type specimen book.</p>

<div class="abs card" style="left:100px">
  <div class="photo" role="img" aria-label="Single-storey commercial retail building under a cloudy sky" style="background:linear-gradient(180deg,#5f9ad8 0%,#b9d1ea 45%,#c9b6a0 70%,#6e6259 100%)"><div class="label">COMMERCIAL</div></div>
</div>
<div class="abs card" style="left:616px">
  <div class="photo" role="img" aria-label="Modern two-storey residence with pool at dusk" style="background:linear-gradient(180deg,#8aa2bd 0%,#d8d2c8 40%,#a88560 65%,#4c7f95 100%)"><div class="label">RESIDENTIAL</div></div>
</div>

<section class="abs projects"></section>
<h2 class="abs section-title" style="top:1194px">LASTEST <em>PROJECTS</em></h2>
<div class="abs filters"><span class="active">ALL</span><span>3D DESIGN</span><span>BUILDING</span><span>ART</span><span>EXTERIOR</span><span>INTERIOR</span></div>

<div class="abs tile" style="left:100px" role="img" aria-label="Glass office towers against blue sky" style="background:#4a7fbf"><div style="width:100%;height:100%;background:linear-gradient(135deg,#6fa8dc,#2f5f99 60%,#b59a7a)"></div></div>
<div class="abs tile tile-overlay" style="left:353px;background:linear-gradient(180deg,#3c4650,#1f2a33)" role="img" aria-label="Modern office building rendering with dark overlay">
  <span class="t1">3D DESIGN</span><span class="t2">QUALITY CONSTRUCTOR</span>
  <svg width="14" height="14" viewBox="0 0 12 12"><circle cx="5" cy="5" r="3.8" stroke="#fff" stroke-width="2" fill="none"/><path d="M8 8l3 3" stroke="#fff" stroke-width="2"/></svg>
</div>
<div class="abs tile" style="left:605px;background:linear-gradient(180deg,#5c9de0 0%,#c7c2bb 40%,#7a8a95 65%,#5f9a3c 100%)" role="img" aria-label="Suburban house with dormer windows and front lawn"></div>
<div class="abs tile" style="left:858px;background:linear-gradient(160deg,#e8e4de 0%,#cfc6bb 45%,#a9622e 80%,#7b3f17 100%)" role="img" aria-label="Bright open-plan interior with wooden floor"></div>

<h2 class="abs section-title" style="top:1614px">TESTIMONIALS</h2>

<div class="abs quote" style="left:97px"><span class="mark">&ldquo;</span><p>"We have assembled a project team comprised of the nation's top laboratory design and building professionals and are delighted to have Builder execute our vision for this unprecendented facility."</p><span class="tail"></span></div>
<div class="abs quote" style="left:617px"><span class="mark">&ldquo;</span><p>"We have assembled a project team comprised of the nation's top laboratory design and building professionals and are delighted to have Builder execute our vision for this unprecendented facility."</p><span class="tail"></span></div>

<div class="abs avatar" style="left:117px;top:1833px" role="img" aria-label="Portrait of client"></div>
<div class="abs person" style="left:224px;top:1849px">Mr.Daniel Voss</div>
<div class="abs role" style="left:224px;top:1874px">Founder/CEO of Northgate Studio</div>
<div class="abs avatar" style="left:637px;top:1833px" role="img" aria-label="Portrait of client"></div>
<div class="abs person" style="left:744px;top:1849px">Mis.Helena Voss</div>
<div class="abs role" style="left:744px;top:1874px">Founder/CEO of Northgate Studio</div>

<footer class="abs footer">
  <div class="fcol about" style="left:98px"><h4>ABOUT US</h4><p>Lorem Ipsum is simply dummy text of the printing and typesetting industry. Lorem Ipsum has been the industry's standard dummy text ever since the 1500s, when an unknown printer</p></div>
  <div class="fcol" style="left:345px"><h4>WELCOME</h4><ul><li>Home</li><li>Portfolio</li><li>Product Specs</li><li>Testimonials</li><li>Our Process</li><li>Contact</li></ul></div>
  <div class="fcol" style="left:525px"><h4>CONTACT</h4><ul><li style="line-height:21px">Brenwick Structures</li><li style="line-height:21px">24 Harbor Lane</li><li style="line-height:21px;margin-bottom:6px">Kestrel Bay 7021</li>
    <li class="contact-line"><svg width="8" height="12"><rect x=".5" y=".5" width="7" height="11" rx="1" stroke="#bbb" fill="none"/></svg>0400 555 118</li>
    <li class="contact-line"><svg width="10" height="10"><rect width="10" height="10" fill="#999"/></svg>5550 142 907</li>
    <li class="contact-line"><svg width="10" height="8"><rect width="10" height="8" fill="#999"/></svg>hello@brenwick.example</li></ul></div>
  <div class="fcol" style="left:757px"><h4>INFORMATION</h4><ul><li>Privacy Policy</li><li>Terms &amp; Conditions</li><li>Sitemap</li></ul></div>
  <div class="fcol social" style="left:980px"><h4>FOLLOW US</h4><ul><li><i></i>: Social Page</li><li><i></i>: Updates</li><li><i></i>: Network</li><li><i></i>: Circles</li></ul></div>
</footer>
<div class="abs bottom">Copyrights &copy; Brenwick Structures 2015. All rights reserved.</div>

</body>
</html>
```